New Website for novelty yarn producer

We need a new website for our company, Tarvek. We make highly tailored yarns for weavers worldwide. This year marks our 40th anniversary and we want to evolve our image and identity.

Our temporary website can be found at:
www.tarvekyarns.com

Our only concern in that throughout the website the protagonist must be our client, we make their creations possible and are highly adaptable both during the ideation process of the yarn as well as in the production. This is at the core of the way we do business and is summarised within the concept of FPM (Fluid Partner Method).

Industry/Entity Type

Textile

Number of Pages Required

1 page

Colors
9bcb3c

Requirements
Must have
• Fluid Partner Method (FPM) - can be found on or current website www.tarvekyarns.com

```html
<!DOCTYPE html>
<html lang="en">
<head>
<meta charset="utf-8">
<title>Tarvek – Tailored Weaving Solutions</title>
<link rel="stylesheet" href="https://fonts.googleapis.com/css2?family=Playfair+Display:wght@400;700&family=Lato:wght@400;700&display=swap">
<style>
:root{
  --green:#9bcb3c;
  --ink:#222;
  --text:#444;
  --muted:#777;
  --paper:#fafafa;
  --band:#efefef;
  --white:#fff;
  --footer:#151515;
  --serif:"Playfair Display", Georgia, serif;
  --sans:"Lato", Arial, sans-serif;
}
*{box-sizing:border-box;margin:0;padding:0}
html,body{width:1200px;height:4110px;overflow:hidden}
body{background:var(--paper);font-family:var(--sans);color:var(--text);position:relative}
.abs{position:absolute}
.btn{display:inline-block;background:var(--green);color:var(--white);font:700 12px var(--sans);border-radius:16px;padding:8px 28px;text-align:center}
.btn.light{background:var(--white);color:var(--green)}
h2.section-title{font:700 26px var(--serif);color:var(--ink);text-align:center}

/* header / hero */
.hero{left:0;top:0;width:1200px;height:671px;background:
  radial-gradient(circle at 15% 20%,#e04a7a 0,transparent 22%),
  radial-gradient(circle at 45% 15%,#f08a3c 0,transparent 20%),
  radial-gradient(circle at 80% 25%,#d83a32 0,transparent 22%),
  radial-gradient(circle at 20% 75%,#7a4fc0 0,transparent 24%),
  radial-gradient(circle at 55% 70%,#3aa0d8 0,transparent 24%),
  radial-gradient(circle at 88% 75%,#2d5fc0 0,transparent 22%),
  linear-gradient(135deg,#c84a8a,#e8a040 45%,#4a8ad0);}
.brand{left:520px;top:8px;width:160px;height:84px;background:var(--white);display:flex;flex-direction:column;align-items:center;justify-content:center}
.brand-name{font:700 38px var(--serif);color:var(--ink);letter-spacing:1px}
.menu-icon{left:1058px;top:42px}
.hero-title{left:0;top:330px;width:1200px;text-align:center;font:700 28px var(--serif);color:var(--white);letter-spacing:1px}
.hero-btn{left:546px;top:388px}

/* feature cards */
.feature{top:603px;width:296px;height:293px;background:var(--white);border-radius:18px;box-shadow:0 4px 16px rgba(0,0,0,.12);text-align:center;padding:24px 30px}
.feature h3{font:700 26px var(--serif);color:var(--ink)}
.feature p{font:400 13px/1.45 var(--sans);color:var(--text);margin:14px 0 18px}
.feature .icon{width:74px;height:74px;margin:14px auto 0;border-radius:50%;background:var(--green);display:flex;align-items:center;justify-content:center}
.feature.active{background:var(--green)}
.feature.active h3,.feature.active p{color:var(--white)}
.feature.active .icon{background:transparent}

/* method */
.method-label{left:0;top:1020px;width:1200px;text-align:center;font:400 18px var(--sans);color:var(--muted);letter-spacing:4px}
.method-title{left:0;top:1108px;width:1200px;text-align:center;font:700 26px var(--serif);color:var(--ink)}
.method-title span{color:var(--green)}
.method-text{left:240px;top:1147px;width:720px;text-align:center;font:400 14px/1.5 var(--sans)}
.method-btn{left:546px;top:1228px}

/* story band */
.story{left:0;top:1320px;width:1200px;height:330px;background:var(--band)}
.story-col{top:55px;width:420px;height:215px}
.story-col h3{font:700 24px var(--serif);color:var(--ink)}
.story-col .sub{font:400 13px var(--sans);margin:10px 0 14px}
.story-col p{font:400 13px/1.5 var(--sans)}
.story-col .btn{position:absolute;left:0;top:178px}

/* offer */
.offer-title{left:0;top:1698px;width:1200px}
.offer{top:1775px;width:162px;height:132px;display:flex;flex-direction:column;align-items:center;justify-content:flex-start;padding-top:22px;gap:18px}
.offer span{font:700 25px var(--serif);color:var(--ink)}
.offer.active{background:var(--green)}
.offer.active span{color:var(--white)}

/* team */
.team{left:0;top:1973px;width:1200px;height:383px;background:linear-gradient(160deg,#3a2a28,#6a4a40 40%,#2a1d1c 75%,#4d3530)}
.team .section-title{color:var(--white);position:absolute;left:0;top:34px;width:1200px}
.member{top:115px;height:126px;display:flex;align-items:center}
.member .photo{width:116px;height:116px;border-radius:50%;border:5px solid var(--white);background:radial-gradient(circle at 50% 40%,#d8b8a0,#8a6a58);position:relative;z-index:2}
.member .name{height:126px;margin-left:-56px;padding-left:80px;display:flex;flex-direction:column;justify-content:center;align-items:center;font:700 26px/1.3 var(--serif);text-align:center}
.member.green .name{background:var(--green);color:var(--white);width:290px;border:3px solid var(--white)}
.member.white .name{background:var(--white);color:var(--ink);width:290px;border:3px solid #bbb}
.arrow{width:26px;height:26px;border-radius:50%;display:flex;align-items:center;justify-content:center}
.team-btn{left:540px;top:307px}

/* numbers */
.numbers-title{left:0;top:2405px;width:1200px;line-height:1.3}
.stat{top:2508px;width:300px;text-align:center}
.stat .circle{width:64px;height:64px;margin:0 auto;border-radius:50%;background:var(--green);color:var(--white);font:700 26px/64px var(--serif)}
.stat .label{margin-top:20px;font:400 15px var(--sans);color:var(--text);letter-spacing:.5px}
.numbers-btn{left:540px;top:2670px}

/* blog */
.blog{left:0;top:2767px;width:1200px;height:699px;background:var(--band)}
.blog .section-title{position:absolute;left:0;top:34px;width:1200px}
.post{top:99px;width:296px;height:430px;background:var(--white);padding:16px;box-shadow:0 2px 8px rgba(0,0,0,.08)}
.post .thumb{height:212px}
.post h4{font:700 15px var(--serif);color:var(--ink);margin-top:14px}
.post .meta{font:400 11px var(--sans);margin-top:6px;color:#555}
.post p{font:400 12px/1.5 var(--sans);margin-top:12px}
.post .more{font:400 12px var(--sans);margin-top:8px}
.post.active{background:var(--green)}
.post.active h4,.post.active .meta,.post.active p,.post.active .more{color:var(--white)}
.dots{left:577px;top:566px;display:flex;gap:6px}
.dots i{width:9px;height:9px;border-radius:50%;background:#bbb;display:block}
.dots i:first-child{background:var(--green)}
.blog-btn{left:546px;top:613px}

/* newsletter */
.news-title{left:0;top:3535px;width:1200px}
.news-form{left:323px;top:3598px;width:554px;height:38px;display:flex}
.news-form .field{flex:1;border:1px solid #ccc;border-radius:19px 0 0 19px;background:var(--white);font:400 13px/36px var(--sans);color:#999;padding-left:22px}
.news-form .submit{width:104px;background:var(--green);color:var(--white);border-radius:0 19px 19px 0;font:700 13px/38px var(--sans);text-align:center;letter-spacing:1px}

/* footer */
.footer{left:0;top:3713px;width:1200px;height:397px;background:radial-gradient(circle at 70% 40%,#2a2a2a,var(--footer) 60%)}
.footer .logo{left:123px;top:50px;font:700 42px var(--serif);color:var(--white);letter-spacing:1px}
.footer .about{left:123px;top:120px;width:240px;font:400 13px/1.5 var(--sans);color:var(--white)}
.footer .about a{color:var(--green);text-decoration:none}
.socials{left:123px;top:220px;display:flex;gap:10px}
.socials i{width:28px;height:28px;border:2px solid var(--white);border-radius:50%;display:block}
.footer h5{font:700 17px var(--serif);color:var(--white)}
.links{left:419px;top:46px}
.links ul{list-style:none;margin-top:26px}
.links li{font:700 11px/25px var(--sans);color:var(--white);letter-spacing:1px;padding-left:14px;position:relative}
.links li:before{content:"";position:absolute;left:0;top:11px;width:4px;height:4px;border-radius:50%;background:var(--white)}
.contact{left:696px;top:46px;width:360px}
.contact ul{list-style:none;margin-top:26px}
.contact li{font:400 12px/20px var(--sans);color:var(--white);display:flex;gap:8px;align-items:center}
.contact .legal{font:400 12px/17px var(--sans);color:var(--white);margin-top:4px;padding-left:20px}
.footer .rule{left:123px;top:337px;width:954px;height:1px;background:#555}
.footer .copy{left:123px;top:360px;font:400 12px var(--sans);color:var(--white)}
.footer .terms{left:940px;top:360px;font:400 12px var(--sans);color:var(--white);width:137px;text-align:right}
</style>
</head>
<body>

<section class="hero abs" role="img" aria-label="Close-up photograph of colourful balls of knitting yarn"></section>
<div class="brand abs"><span class="brand-name">TARVEK</span></div>
<svg class="menu-icon abs" width="22" height="18" viewBox="0 0 22 18"><rect y="0" width="22" height="3" fill="#fff"/><rect y="7" width="22" height="3" fill="#fff"/><rect y="14" width="22" height="3" fill="#fff"/></svg>
<h1 class="hero-title abs">TAILORED WEAVING SOLUTIONS</h1>
<span class="btn hero-btn abs">Read More</span>

<article class="feature abs" style="left:129px">
  <h3>Experience</h3>
  <div class="icon"><svg width="38" height="34" viewBox="0 0 38 34" fill="none" stroke="#fff" stroke-width="2.5"><rect x="2" y="9" width="34" height="23" rx="3"/><path d="M13 9V4h12v5M2 19h34"/></svg></div>
  <p>Over the years the company has gained the knowledge and skills that define the supp...</p>
  <span class="btn">Read More</span>
</article>
<article class="feature active abs" style="left:452px">
  <h3>Creativity</h3>
  <div class="icon"><svg width="44" height="48" viewBox="0 0 44 48" fill="none" stroke="#fff" stroke-width="2.5"><path d="M22 8a12 12 0 0 0-7 22v6h14v-6a12 12 0 0 0-7-22zM16 41h12M22 1v3M5 14l3 2M39 14l-3 2"/></svg></div>
  <p>Our belief is that the key to our clients' success is a combination of innovation, creativi...</p>
  <span class="btn light">Read More</span>
</article>
<article class="feature abs" style="left:767px">
  <h3>Professionality</h3>
  <div class="icon" style="background:transparent;border:2px solid var(--green)"><svg width="40" height="46" viewBox="0 0 40 46" fill="none" stroke="#9bcb3c" stroke-width="2.5"><circle cx="20" cy="16" r="12"/><path d="M12 26l-5 16 8-4 5 6 5-6M28 26l5 16-8-4"/></svg></div>
  <p>We are a family business at the core. Our company is run with the same values as the fam...</p>
  <span class="btn">Read More</span>
</article>

<p class="method-label abs">FLUID PARTNER METHOD</p>
<h2 class="method-title abs"><span>TVYS</span> Fluid Partner Method</h2>
<p class="method-text abs">We believe that the key to delivering a yarn that exceeds our client's expectation is to work together with weavers from step one, starting from the desired end product and working backwards. This allows us to develop the product that our weavers need, rather than having weavers adapt to the supplied raw materials.</p>
<span class="btn method-btn abs">Read More</span>

<section class="story abs">
  <div class="story-col abs" style="left:123px">
    <h3>Our Story</h3>
    <p class="sub">Our story, 40 years in the making</p>
    <p>Lorem Ipsum is simply dummy text of the printing and typesetting industry. Lorem Ipsum has been the industry's standard dummy text ever since the 1500s, when an unknown printer took a galley of type and scrambled it to make a type specimen book.</p>
    <span class="btn">Read More</span>
  </div>
  <div class="story-col abs" style="left:663px">
    <h3>About us</h3>
    <p class="sub">TVYS combines the experience of a team</p>
    <p>TVYS combines the experience of a team that has served the weaving industry for over 40 years, fully dedicated to the success of our clients</p>
    <span class="btn">Read More</span>
  </div>
</section>

<h2 class="section-title offer-title abs">What we offer</h2>
<div class="offer abs" style="left:283px"><svg width="46" height="46" viewBox="0 0 46 46" fill="none" stroke="#9bcb3c" stroke-width="2.5"><circle cx="23" cy="23" r="19"/><path d="M4 23h38M23 4c-8 10-8 28 0 38M23 4c8 10 8 28 0 38"/></svg><span>Network</span></div>
<div class="offer active abs" style="left:512px"><svg width="58" height="40" viewBox="0 0 58 40" fill="none" stroke="#fff" stroke-width="2.5"><path d="M3 5h32v24H3zM35 13h11l8 9v7H35"/><circle cx="13" cy="32" r="5"/><circle cx="44" cy="32" r="5"/></svg><span>Logistics</span></div>
<div class="offer abs" style="left:741px"><svg width="50" height="46" viewBox="0 0 50 46" fill="none" stroke="#9bcb3c" stroke-width="2.5"><path d="M3 43V22l11-7v7l11-7v7l11-7v28zM40 43V4h6v39M3 43h46"/></svg><span>Production</span></div>

<section class="team abs" role="img" aria-label="Close-up photograph of woven fabric in dark red and brown">
  <h2 class="section-title">Our Team</h2>
  <div class="arrow abs" style="left:42px;top:173px;background:var(--green)"><svg width="10" height="12" viewBox="0 0 10 12"><path d="M8 1L2 6l6 5" fill="none" stroke="#fff" stroke-width="2"/></svg></div>
  <div class="member green abs" style="left:241px"><div class="photo" role="img" aria-label="Portrait photograph of a team member"></div><div class="name">Marco<br>BELLINI</div></div>
  <div class="member white abs" style="left:622px"><div class="photo" role="img" aria-label="Portrait photograph of a team member"></div><div class="name">Silvia<br>RANIERI</div></div>
  <div class="arrow abs" style="left:1130px;top:173px;background:var(--white)"><svg width="10" height="12" viewBox="0 0 10 12"><path d="M2 1l6 5-6 5" fill="none" stroke="#222" stroke-width="2"/></svg></div>
  <span class="btn team-btn abs">View More</span>
</section>

<h2 class="section-title numbers-title abs">TVYS in Numbers<br>2017</h2>
<div class="stat abs" style="left:121px"><div class="circle">40</div><div class="label">YEARS IN BUSINESS</div></div>
<div class="stat abs" style="left:450px"><div class="circle">2</div><div class="label">MILLION KILOGRAMS/ YR</div></div>
<div class="stat abs" style="left:779px"><div class="circle">8</div><div class="label">BRANDS</div></div>
<span class="btn numbers-btn abs">Find out More</span>

<section class="blog abs">
  <h2 class="section-title">Tarvek Yarn Blog</h2>
  <article class="post active abs" style="left:121px">
    <div class="thumb" role="img" aria-label="Photograph of yarn balls and knitting needles on a table" style="background:linear-gradient(135deg,#e8e0d4,#b89070 60%,#6a4a38)"></div>
    <h4>Blog Title 1</h4>
    <p class="meta">By &nbsp; PETER ALDEN<br>Feb 19,2018</p>
    <p>Lorem Ipsum is simply dummy text of the printing and typesetting industry. Lorem Ipsum has been the industry's standard dummy text.</p>
    <p class="more">Read More ...</p>
  </article>
  <article class="post abs" style="left:455px">
    <div class="thumb" role="img" aria-label="Photograph of pink and coral yarn balls" style="background:linear-gradient(135deg,#f0a0a8,#d85a70 55%,#e8c8c0)"></div>
    <h4>LOREAM IPSUM</h4>
    <p class="meta">By &nbsp; PETER ALDEN<br>Feb 19,2018</p>
    <p>Lorem Ipsum is simply dummy text of the printing and typesetting industry. Lorem Ipsum has been the industry's standard dummy text.</p>
    <p class="more">Read More ...</p>
  </article>
  <article class="post abs" style="left:786px">
    <div class="thumb" role="img" aria-label="Photograph of hands holding a teal yarn ball" style="background:linear-gradient(135deg,#6a7a78,#5ab0b0 50%,#2a3a3a)"></div>
    <h4>LOREAM IPSUM</h4>
    <p class="meta">By &nbsp; PETER ALDEN<br>Feb 19,2018</p>
    <p>Lorem Ipsum is simply dummy text of the printing and typesetting industry. Lorem Ipsum has been the industry's standard dummy text.</p>
    <p class="more">Read More ...</p>
  </article>
  <div class="dots abs"><i></i><i></i><i></i></div>
  <span class="btn blog-btn abs">View More</span>
</section>

<h2 class="section-title news-title abs">Subscribe To Our Newsletter</h2>
<form class="news-form abs"><span class="field">Your E-Mail</span><span class="submit">SUBMIT</span></form>

<footer class="footer abs">
  <div class="logo abs">TARVEK</div>
  <p class="about abs">TVYS combines the experience of a team that has served the weaving industry for over 40 yea...<br><a>Read More ...</a></p>
  <div class="socials abs"><i></i><i></i><i></i></div>
  <div class="links abs">
    <h5>Quick Link</h5>
    <ul><li>HOME</li><li>ABOUT US</li><li>FLUID PARTNER METHOD</li><li>HERITAGE</li><li>TEAM</li><li>BLOG</li><li>CONTACT</li></ul>
  </div>
  <div class="contact abs">
    <h5>Contact Us</h5>
    <ul>
      <li><svg width="10" height="14" viewBox="0 0 10 14"><path d="M5 0a5 5 0 0 0-5 5c0 4 5 9 5 9s5-5 5-9a5 5 0 0 0-5-5z" fill="#fff"/></svg>Via dei Tessitori 12 - 50100 Florence - Italy</li>
      <li><svg width="12" height="12" viewBox="0 0 12 12"><path d="M2 0l3 3-2 2a8 8 0 0 0 4 4l2-2 3 3-2 2C5 12 0 7 0 2z" fill="#fff"/></svg>0555 10482</li>
      <li><svg width="12" height="12" viewBox="0 0 12 12"><rect x="1" y="1" width="10" height="10" fill="none" stroke="#fff" stroke-width="1.5"/></svg>0555 10499</li>
      <li><svg width="12" height="10" viewBox="0 0 12 10"><path d="M0 0h12v10H0zM0 0l6 5 6-5" fill="none" stroke="#fff" stroke-width="1.5"/></svg>sales@tarvekyarns.com</li>
    </ul>
    <p class="legal">R.E.A. FI 481205 - Reg. Imp. FI 0481205776<br>P. IVA 04812057761 - Cod. Fisc. 04812057761<br>Capitale sociale € 120.000,00 i.v.</p>
  </div>
  <div class="rule abs"></div>
  <p class="copy abs">CopyRight © &nbsp;2018 Tarvek. &nbsp;All Right Reserve</p>
  <p class="terms abs">Terms &amp; Conditions</p>
</footer>

</body>
</html>
```